My Journey - Document to be Laminated

I need a document that is professionally designed. Attached are the files that you are needed to produce this document. The main file to follow is called "My Journey - DOC". I would like you to take the concept and produce it professionally. I think it is important to know that this is something that will be laminated and used by door-to-door representatives. So I need it to be designed in Photoshop so that I can change the pictures as needed to fit other students. The students go to the doors and share literature to help people with their health and to grow spiritually. This document will be something they will share to help the people at the door understand who they are and some of their goals in life. If possible, I would like the concept(s) of the attached picture "theme" to be in the background of all the images - but I still don't want it to be busy, so if it is even something in vector background that is fine.

Not sure why the upload function is not working on brush harbor for this project. So to download the files, please see the following link: https://www.parcelnook.net/sh/qk/tbwelx83pazrqumvhnse/Pics-for-Document.zip?key=wjd61mrtp0acqe5vyx8nbh4kz&tk=7pgh2wme&dl=0

Requirements
Should not have
• anyone with jewelry, more on the minimalistic side

```html
<!DOCTYPE html>
<html lang="en">
<head>
<meta charset="utf-8">
<title>My Journey</title>
<link href="https://fonts.googleapis.com/css2?family=Barlow:wght@500;600;700;800&display=swap" rel="stylesheet">
<style>
  :root {
    --page-bg: #c9c9c9;
    --sky-top: #5668a6;
    --sky-mid: #9a8ab4;
    --glow: #f2b25a;
    --sun: #f7c766;
    --earth: #8a3c16;
    --earth-dark: #2a120b;
    --cliff: #3a1f16;
    --card: #f8f8fb;
    --card-edge: #c3262d;
    --label: #2f63ad;
    --title-stroke: #3a6cc0;
    --white: #ffffff;
    --ink: #111111;
  }
  * { box-sizing: border-box; margin: 0; padding: 0; }
  html, body { width: 1200px; height: 679px; overflow: hidden; }
  body {
    background: var(--page-bg);
    font-family: "Barlow", Arial, sans-serif;
    position: relative;
  }
  .poster {
    position: absolute;
    left: 374px; top: 20px;
    width: 452px; height: 639px;
    overflow: hidden;
    box-shadow: 0 6px 18px rgba(0,0,0,.25);
  }
  .poster-backdrop {
    position: absolute; inset: 0;
    background:
      radial-gradient(ellipse 60% 35% at 78% 62%, var(--sun) 0%, rgba(242,178,90,.6) 40%, rgba(242,178,90,0) 75%),
      linear-gradient(180deg, var(--sky-top) 0%, var(--sky-mid) 22%, #d9a88a 42%, var(--glow) 56%, var(--earth) 76%, var(--earth-dark) 100%);
  }
  .poster-backdrop::before {
    content: ""; position: absolute; left: 0; top: 0; width: 150px; height: 100%;
    background: linear-gradient(90deg, var(--cliff) 0%, rgba(58,31,22,.75) 45%, rgba(58,31,22,0) 100%);
  }
  .title {
    position: absolute; left: 58px; top: 40px;
    font-size: 57px; font-weight: 800; line-height: 1;
    color: var(--white); letter-spacing: 0.5px;
    -webkit-text-stroke: 2px var(--title-stroke);
    paint-order: stroke fill;
    text-shadow: 0 2px 3px rgba(0,0,0,.25);
    white-space: nowrap;
  }
  .intro {
    position: absolute; left: 60px; top: 103px;
    font-size: 15.5px; font-weight: 600; color: var(--white);
    text-shadow: 0 1px 2px rgba(0,0,0,.35);
    white-space: nowrap;
  }
  .flow { position: absolute; inset: 0; }
  .story-card {
    position: absolute;
    background: var(--card);
    border: 2px solid var(--card-edge);
    border-radius: 6px;
    padding: 6px 6px 0;
    box-shadow: 0 6px 12px rgba(0,0,0,.3);
    text-align: center;
  }
  .story-card .photo { width: 100%; border-radius: 6px; }
  .story-card .label {
    display: block; color: var(--label);
    font-weight: 600; font-size: 14px; line-height: 24px;
  }
  .card-roots { left: 42px; top: 153px; width: 146px; transform: rotate(-7deg); }
  .card-roots .photo { height: 74px; background: linear-gradient(160deg, #a9c6d8, #d7dcd6 55%, #b8d0de); }
  .card-growing { left: 290px; top: 214px; width: 120px; transform: rotate(8deg); }
  .card-growing .photo { height: 98px; background: linear-gradient(180deg, #cfc6c3, #e9e3d8 60%, #8c8583); }
  .card-family { left: 42px; top: 306px; width: 224px; transform: rotate(3deg); }
  .card-family .photo { height: 104px; background: linear-gradient(180deg, #aab3ba, #6b625c 55%, #2e2c2d); }
  .card-dream { left: 267px; top: 448px; width: 146px; transform: rotate(-5deg); }
  .card-dream .photo { height: 74px; background: linear-gradient(180deg, #b9a99d, #d9b98e 45%, #5a5654); }
  .brand {
    position: absolute; left: 30px; top: 545px; width: 170px;
    display: flex; flex-direction: column; align-items: center; gap: 6px;
  }
  .brand-mark { width: 26px; height: 26px; border-radius: 50%; background: var(--card-edge); }
  .brand-name { font-size: 12.5px; font-weight: 700; color: var(--card-edge); letter-spacing: .4px; white-space: nowrap; }
  .brand-tagline { font-size: 8.5px; font-weight: 500; color: var(--white); white-space: nowrap; }
</style>
</head>
<body>
  <main class="poster">
    <div class="poster-backdrop" role="img" aria-label="Sunset mountain scene with silhouetted climbers helping each other up a cliff"></div>

    <h1 class="title">MY JOURNEY</h1>
    <p class="intro">Hi, my name is [ Your Name ] and this is my story.</p>

    <svg class="flow" width="452" height="639" viewBox="0 0 452 639" aria-hidden="true">
      <defs>
        <marker id="arrowhead" viewBox="0 0 10 10" refX="8" refY="5" markerWidth="6" markerHeight="6" orient="auto">
          <path d="M0 0 L10 5 L0 10 Z" fill="#111"/>
        </marker>
      </defs>
      <g fill="none" stroke="#111" stroke-width="1.8" stroke-dasharray="7 5">
        <path d="M190 190 C240 180 282 204 298 244" marker-end="url(#arrowhead)"/>
        <path d="M416 300 C428 362 392 392 330 392 C302 392 286 388 270 383" marker-end="url(#arrowhead)"/>
        <path d="M128 450 C140 492 190 507 258 504" marker-end="url(#arrowhead)"/>
      </g>
    </svg>

    <figure class="story-card card-roots">
      <div class="photo" role="img" aria-label="Map of Mexico with a pin marking Mexico City"></div>
      <figcaption class="label">My Roots</figcaption>
    </figure>
    <figure class="story-card card-growing">
      <div class="photo" role="img" aria-label="Childhood photo of three young sisters"></div>
      <figcaption class="label">Growing Up</figcaption>
    </figure>
    <figure class="story-card card-family">
      <div class="photo" role="img" aria-label="Family selfie of four people"></div>
      <figcaption class="label">My Family</figcaption>
    </figure>
    <figure class="story-card card-dream">
      <div class="photo" role="img" aria-label="Graduate in cap and gown overlooking a city skyline at sunset"></div>
      <figcaption class="label">My Dream</figcaption>
    </figure>

    <footer class="brand">
      <span class="brand-mark"></span>
      <span class="brand-name">NORTHFIELD YOUTH PROGRAM</span>
      <span class="brand-tagline">Guiding Young Lives Since 2006</span>
    </footer>
  </main>
</body>
</html>
```